Electrical Contractor Company Profile

We need a Brochure that is more entertaining than our current Company Profile Document. We have lots of great experience and awesome looking jobs in our portfolio but need a document that we can either print of send in electronic format to accompany some of our submissions.

We are ideally looking for something 9-10 pages in A4 with some of the pages opening out to A3.

We are looking for a document that is professional and smart however shows the colour and quality that we feel we offer to prospective clientele.

I have included the current Company Profile and Logo along with a number of images of completed projects that may be of use.

Target Market(s)

Builders, Facility Managers, Engineers, Decision makers

Industry/Entity Type

Electrical

Font styles to use
Sans Serif

Colors

Designer to choose colors to be used in the design.

Requirements
Must have
• - Modern look with a focus on sustainability
• - Clean Simple and Professional
• - Incorporate our Logo
• Core Business Lines need to be across an A3 opening page and have photos relating to these lines Solar, Communications and any of the projects.
Nice to have
• Lots of colour and photos mixed with the text
Should not have
• Lightning bolts or corny symbols

```html
<!DOCTYPE html>
<html lang="en">
<head>
<meta charset="utf-8">
<title>Lumen Electrical – Company Profile Spread</title>
<link href="https://fonts.googleapis.com/css2?family=Open+Sans:wght@400;600;700;800&display=swap" rel="stylesheet">
<style>
  :root{
    --orange:#e17a2e;
    --navy:#2a3a8e;
    --ink:#2b2f3a;
    --paper:#ffffff;
    --stage:#d9dadd;
  }
  *{box-sizing:border-box;margin:0;padding:0}
  html,body{width:1200px;height:789px;overflow:hidden;background:var(--stage);font-family:"Open Sans",Arial,sans-serif;color:var(--ink)}
  .spread{position:absolute;left:105px;top:44px;width:990px;height:700px;display:flex;box-shadow:0 8px 30px rgba(0,0,0,.25)}
  .page{position:relative;width:495px;height:700px;background:var(--paper);overflow:hidden}
  .page--left{box-shadow:inset -14px 0 18px -14px rgba(0,0,0,.25)}
  .page--right{box-shadow:inset 14px 0 18px -14px rgba(0,0,0,.25)}
  .photo{position:absolute}
  .photo--building{left:150px;top:28px;width:345px;height:205px;background:linear-gradient(160deg,#dfe6ee 0%,#c9ced6 45%,#6d7a5c 80%,#3f4a34 100%)}
  .photo--switchboard{left:0;top:200px;width:360px;height:275px;background:linear-gradient(120deg,#d9d9d9 0%,#9a8f86 30%,#e58a2a 55%,#c56a1c 80%,#efefef 100%)}
  .photo--atrium{left:0;top:372px;width:395px;height:228px;background:radial-gradient(circle at 45% 45%,#e8edf2 0%,#8b96a6 35%,#3a4350 70%,#232a33 100%)}
  .quote{position:absolute;background:var(--orange);color:#fff;padding:16px 18px 14px 26px;font-size:8.5px;line-height:1.45}
  .quote::before{content:"\201C";position:absolute;left:8px;top:2px;font-size:22px;opacity:.5}
  .quote::after{content:"\201D";position:absolute;right:10px;bottom:-6px;font-size:22px;opacity:.5}
  .quote__author{display:block;font-weight:700;margin-top:2px}
  .quote--one{left:285px;top:178px;width:200px}
  .quote--two{left:240px;top:430px;width:230px}
  .quote--three{left:240px;top:500px;width:235px}
  .brand{position:absolute;display:flex;align-items:center;gap:9px;color:var(--navy);font-weight:800;font-size:21px;letter-spacing:.5px}
  .brand__mark{width:26px;height:26px;border-radius:50%;background:var(--orange)}
  .page--left .brand{left:38px;top:545px}
  .page--right .brand{left:38px;top:625px}
  .web-band{position:absolute;height:30px;background:var(--orange);color:#fff;font-size:11px;font-weight:600;display:flex;align-items:center;justify-content:center;gap:7px}
  .web-band svg{width:11px;height:11px}
  .page--left .web-band{left:225px;top:600px;width:270px}
  .page--right .web-band{left:225px;top:660px;width:245px}
  .tab{position:absolute;left:125px;top:38px;width:320px;height:40px;background:var(--orange);color:#fff;font-size:15px;display:flex;align-items:center;padding-left:22px}
  .copy{position:absolute;left:38px;top:92px;width:415px}
  .intro{font-size:7.5px;line-height:1.4;margin-bottom:10px}
  .heading{color:var(--navy);font-size:13px;font-weight:600;margin-bottom:6px}
  .para{font-size:7.5px;line-height:1.4;margin-bottom:14px}
  .checklist{list-style:none;font-size:9.5px;line-height:1.35}
  .checklist li{position:relative;padding-left:14px}
  .checklist li::before{content:"";position:absolute;left:2px;top:3px;width:4px;height:7px;border:solid var(--orange);border-width:0 1.6px 1.6px 0;transform:rotate(40deg)}
</style>
</head>
<body>
<div class="spread">

  <section class="page page--left">
    <div class="photo photo--building" role="img" aria-label="Photo of the completed sports centre building with curved white facade and landscaped entry"></div>
    <div class="photo photo--switchboard" role="img" aria-label="Photo of an open orange main switchboard with wired panels"></div>
    <blockquote class="quote quote--one">The finished product at the Westbay Sports Centre was of excellent quality. We were extremely impressed with the ease of use and high levels of communication we received.
      <span class="quote__author">Daniel Marsh, Halden Constructions</span></blockquote>
    <blockquote class="quote quote--two">The finished product is of excellent quality, and we have been extremely impressed with the ease of use and high levels of communication received.
      <span class="quote__author">Paul Keaton, Northgate Property Centre</span></blockquote>
    <div class="brand"><span class="brand__mark"></span>LUMEN ELECTRICAL</div>
    <div class="web-band">
      <svg viewBox="0 0 12 12" aria-hidden="true"><circle cx="6" cy="6" r="5" fill="none" stroke="#fff" stroke-width="1.2"/><path d="M1 6h10M6 1c-2.5 3-2.5 7 0 10M6 1c2.5 3 2.5 7 0 10" fill="none" stroke="#fff" stroke-width="1"/></svg>
      www.lumenelectrical.com.au</div>
  </section>

  <section class="page page--right">
    <div class="tab">Proven Management Systems</div>
    <div class="copy">
      <p class="intro">Our commitment to quality, health and safety and the environment places Lumen Electrical Services apart from our many competitors.</p>
      <h2 class="heading">Quality</h2>
      <p class="para">Lumen Electrical Services is committed to providing clients with exceptional products and services in a creative and innovative manner. With our Integrated Management System aligned to ISO9001:2008 we ensure a consistent result is achieved in all cases.</p>
      <h2 class="heading">Our Quality system ensures:</h2>
      <ul class="checklist">
        <li>Consistent communication with all stakeholders</li>
        <li>Experienced and qualified staff are employed who are committed to company vision and commitment to quality</li>
        <li>Flexible workforce whereby staff are able to work across all lines of business;</li>
        <li>Internal systems and software that allow thorough reporting and auditing;</li>
        <li>Clearly defined roles and responsibilities for all staff;</li>
        <li>Correct training and support for all staff;</li>
        <li>Quality monitoring and reporting throughout the entire work process.</li>
      </ul>
    </div>
    <div class="photo photo--atrium" role="img" aria-label="Photo looking up into a building atrium with a coloured lattice ceiling and feature lighting"></div>
    <blockquote class="quote quote--three">We found them to be professional, courteous and able to carry out their works both on time and on budget. We will be happy to see Lumen on future projects.
      <span class="quote__author">Daniel Marsh, Halden Constructions</span></blockquote>
    <div class="brand"><span class="brand__mark"></span>LUMEN ELECTRICAL</div>
    <div class="web-band">
      <svg viewBox="0 0 12 12" aria-hidden="true"><circle cx="6" cy="6" r="5" fill="none" stroke="#fff" stroke-width="1.2"/><path d="M1 6h10M6 1c-2.5 3-2.5 7 0 10M6 1c2.5 3 2.5 7 0 10" fill="none" stroke="#fff" stroke-width="1"/></svg>
      www.lumenelectrical.com.au</div>
  </section>

</div>
</body>
</html>
```